New Business Card Design*

We are a recruitment company based in Norwich/Cambridge England.
I have included our company logo which we want to remain the same.

What we are looking for is a new creative Business card which will really stand out!!

Contact Information for Business Card

Harriet Vance
email: Harriet@brelvix.co.uk
Address: Tolworth House
Ashgrove Innovation Park
Pelham Road
Norwich
KT9 3QD
Tel:01632 960418

```html
<!DOCTYPE html>
<html lang="en">
<head>
<meta charset="utf-8">
<title>Business Card Concept – Brelvix</title>
<link rel="stylesheet" href="https://fonts.googleapis.com/css2?family=Open+Sans:wght@400;600;700&display=swap">
<style>
  :root {
    --backdrop: #c8c8c8;
    --caption: #7a7a7a;
    --card-white: #ffffff;
    --brand-green: #8cc63f;
    --ink: #3a3a3a;
    --icon-grey: #a3a3a3;
    --tag-grey: #8a8a8a;
  }
  * { margin: 0; padding: 0; box-sizing: border-box; }
  html, body { width: 1200px; height: 1200px; overflow: hidden; }
  body {
    position: relative;
    background: var(--backdrop);
    font-family: "Open Sans", Arial, sans-serif;
  }
  .concept-title {
    position: absolute;
    left: 56px; top: 36px;
    font-size: 24px;
    font-weight: 400;
    color: var(--caption);
    letter-spacing: 0.2px;
  }
  .card {
    position: absolute;
    top: 191px;
    width: 391px; height: 254px;
    overflow: hidden;
  }
  .card--front { left: 133px; background: var(--card-white); }
  .card--back { left: 672px; background: var(--brand-green); }

  .corner-shape { position: absolute; left: 0; top: 0; width: 391px; height: 254px; }

  .brand { position: absolute; display: flex; align-items: center; }
  .brand__dot { border-radius: 50%; flex: none; }
  .brand__name { font-weight: 700; line-height: 1; }
  .brand__tag { position: absolute; font-size: 5px; letter-spacing: 1.6px; font-weight: 600; white-space: nowrap; }

  .card--front .brand { left: 51px; top: 40px; }
  .card--front .brand__dot { width: 30px; height: 30px; background: var(--brand-green); margin-right: 8px; }
  .card--front .brand__name { font-size: 29px; color: var(--brand-green); }
  .card--front .brand__tag { left: 38px; top: 33px; color: var(--tag-grey); }

  .holder-name {
    position: absolute; left: 245px; top: 53px;
    font-size: 16px; font-weight: 600; color: var(--ink);
  }
  .contact { position: absolute; left: 212px; top: 106px; list-style: none; }
  .contact__item { display: flex; align-items: flex-start; font-size: 10.5px; color: var(--ink); line-height: 13.6px; }
  .contact__item + .contact__item { margin-top: 18px; }
  .contact__item:nth-child(3) { margin-top: 17px; }
  .contact__icon { width: 19px; height: 19px; flex: none; margin-right: 14px; margin-top: -2px; }

  .card--back .brand { left: 72px; top: 80px; }
  .card--back .brand__dot { width: 56px; height: 56px; background: var(--card-white); margin-right: 12px; }
  .card--back .brand__name { font-size: 40px; color: var(--card-white); }
  .card--back .brand__tag { left: 70px; top: 50px; color: var(--card-white); font-size: 6px; letter-spacing: 2px; }
  .web-address {
    position: absolute; left: 0; right: 0; top: 190px;
    text-align: center; font-size: 14px; font-weight: 700; color: var(--card-white);
  }
</style>
</head>
<body>
  <h1 class="concept-title">Business Card Concept for Brelvix.co.uk</h1>

  <section class="card card--front" aria-label="Card front">
    <svg class="corner-shape" viewBox="0 0 391 254" aria-hidden="true">
      <path d="M0,83 C70,100 160,170 186,254 L0,254 Z" fill="var(--brand-green)"/>
      <path d="M0,161 C45,175 90,210 107,254 L0,254 Z" fill="var(--card-white)"/>
    </svg>
    <div class="brand">
      <span class="brand__dot"></span>
      <span class="brand__name">Brelvix</span>
      <span class="brand__tag">Technology Recruitment</span>
    </div>
    <h2 class="holder-name">Harriet Vance</h2>
    <ul class="contact">
      <li class="contact__item">
        <svg class="contact__icon" viewBox="0 0 20 20" aria-hidden="true"><circle cx="10" cy="10" r="10" fill="var(--icon-grey)"/><text x="10" y="13.5" text-anchor="middle" font-size="10" fill="#fff" font-family="Open Sans, sans-serif">@</text></svg>
        <span>harriet@brelvix.co.uk</span>
      </li>
      <li class="contact__item">
        <svg class="contact__icon" viewBox="0 0 20 20" aria-hidden="true"><circle cx="10" cy="10" r="10" fill="var(--icon-grey)"/><path d="M6.5,5 L8.5,5 L9.3,7.8 L8,8.8 C8.7,10.4 9.6,11.3 11.2,12 L12.2,10.7 L15,11.5 L15,13.5 C10,14 6,10 6.5,5 Z" fill="#fff"/></svg>
        <span>01632 960418</span>
      </li>
      <li class="contact__item">
        <svg class="contact__icon" viewBox="0 0 20 20" aria-hidden="true"><circle cx="10" cy="10" r="10" fill="var(--icon-grey)"/><path d="M10,4 C7.5,4 6,5.8 6,8 C6,11 10,15.5 10,15.5 C10,15.5 14,11 14,8 C14,5.8 12.5,4 10,4 Z" fill="#fff"/><circle cx="10" cy="8" r="1.6" fill="var(--icon-grey)"/></svg>
        <address style="font-style:normal">Tolworth House<br>Ashgrove Innovation Park<br>Pelham Road<br>Norwich, KT9 3QD</address>
      </li>
    </ul>
  </section>

  <section class="card card--back" aria-label="Card back">
    <div class="brand">
      <span class="brand__dot"></span>
      <span class="brand__name">Brelvix</span>
      <span class="brand__tag">Technology Recruitment</span>
    </div>
    <p class="web-address">www.brelvix.co.uk</p>
  </section>
</body>
</html>
```